Lien Post Card - (5.5 x 8.5)

FRONT OF POSTCARD
Is a Property Lien Putting Your Home at Risk?
HOA Liens • Tax Liens • Municipal Charges • Other Property-Related Liens
You may have options to resolve outstanding liens and protect your home.
A Refinance or Home Equity Line of Credit (HELOC) may help you:
✔ Pay off qualifying liens
✔ Consolidate debt into one manageable payment
✔ Access your home's equity
✔ Improve your financial flexibility
✔ Avoid additional penalties, fees, or collection actions
Don't wait until the situation becomes more difficult.
Call today for a confidential review of your options.
Bluecove Lending Group, Inc.
(800) 641-2907 x 42
www.bluecovelending.com
NMLS #738150
BACK OF POSTCARD
Your Home Equity Could Be the Solution
If you have received notices regarding:
• Delinquent Property Taxes
• HOA or Condo Association Assessments
• Municipal Utility Liens
• Special Assessments
• Other Property-Related Obligations
You may qualify for financing options designed to help satisfy those obligations and bring your property current.
Our experienced mortgage professionals can review your situation and discuss available programs, including:
• Cash-Out Refinancing
• Home Equity Lines of Credit (HELOCs)
• Home Equity Loans
• Debt Consolidation Solutions
Free Consultation • No Obligation
Contact Marcus Whitfield today at (800) 641-2907 x42 or mwhitfield@bluecovelending.com (NMLS #84617)

```html
<!DOCTYPE html>
<html lang="en">
<head>
<meta charset="utf-8">
<title>Bluecove Lending Group – Lien Postcard</title>
<link href="https://fonts.googleapis.com/css2?family=Noto+Serif:wght@700&family=Roboto:wght@400;500;700&display=swap" rel="stylesheet">
<style>
:root{
  --navy:#0b1a4e;
  --navy-2:#1c3784;
  --gold:#f0c565;
  --gold-deep:#dba53a;
  --gold-light:#fbe4a3;
  --sky:#4f7bbf;
  --cream:#fbecc6;
  --ink:#0d1f5c;
  --heading:#13357f;
  --body:#1e2436;
  --page:#a9a9a9;
}
*{box-sizing:border-box;margin:0;padding:0}
html,body{width:954px;height:1200px;overflow:hidden}
body{background:var(--page);font-family:"Roboto",Arial,sans-serif;position:relative}
.card{position:absolute;left:74px;width:806px;height:521px;background:#fff;overflow:hidden;box-shadow:0 6px 18px rgba(0,0,0,.35)}
.card--front{top:63px}
.card--back{top:616px}
.abs{position:absolute}
.header-band{position:absolute;left:0;top:0}
.headline{position:absolute;left:47px;font-family:"Noto Serif",Georgia,serif;font-weight:700;color:#fff;font-size:32.4px;line-height:37px;white-space:nowrap}
.headline .gold{color:var(--gold)}
.headline .sky{color:var(--sky)}
.brand{position:absolute;left:566px;top:50px;width:198px;display:flex;align-items:center;gap:8px}
.brand__dot{width:26px;height:26px;border-radius:50%;background:var(--sky);flex:none}
.brand__name{font-family:"Roboto",Arial,sans-serif;font-weight:700;font-size:17px;line-height:20px;color:var(--navy)}
.photo{position:absolute}
.photo--city{left:388px;top:131px;width:418px;height:347px;
  background:linear-gradient(90deg,#fff 0%,rgba(255,255,255,0) 30%),
  linear-gradient(180deg,#e8e8e8 0%,#a8a8a8 40%,#b8763a 68%,#6a3416 88%,#3c1a0c 100%)}
.photo--advisor{left:427px;top:253px;width:379px;height:225px;
  background:linear-gradient(90deg,#fff 0%,rgba(255,255,255,0) 25%),
  linear-gradient(180deg,#fff 0%,#d6d6d6 45%,#8e8e8e 100%)}
.icon-item{position:absolute;display:flex;align-items:center;transform:translateY(-50%)}
.ring{border-radius:50%;background:#fff;border:2px solid var(--gold);box-shadow:0 0 0 1.5px var(--heading);display:flex;align-items:center;justify-content:center;flex:none}
.ring svg{fill:var(--heading)}
.icon-label{font-size:11px;line-height:15px;color:var(--body);margin-left:8px;white-space:nowrap}
.front-icons .ring{width:40px;height:40px}
.back-icons .ring{width:37px;height:37px}
.back-icons .icon-label{font-size:9.5px;line-height:12px;margin-left:7px}
.cream-band{position:absolute;left:0}
.lead-serif{position:absolute;left:47px;font-family:"Noto Serif",Georgia,serif;font-weight:700;font-size:14.9px;line-height:19.5px;color:var(--ink);white-space:nowrap}
.subhead{position:absolute;left:47px;font-weight:500;color:var(--heading);font-size:15px;line-height:21px;white-space:nowrap}
.checklist{position:absolute;left:46px;list-style:none}
.checklist li{display:flex;align-items:center;height:20px;font-size:11px;color:var(--body);white-space:nowrap}
.checklist svg{width:12px;height:12px;margin-right:8px;flex:none}
.closing{position:absolute;left:47px;font-weight:500;color:var(--ink);font-size:14.5px;line-height:21px}
.footer-bar{position:absolute;left:0;top:478px;width:806px;height:43px}
.footer-cta{position:absolute;left:24px;top:0;height:43px;display:flex;align-items:center;font-weight:700;color:var(--ink);white-space:nowrap}
.contact{position:absolute;right:18px;top:0;height:43px;display:flex;align-items:center;gap:16px;color:#fff;font-size:11px;white-space:nowrap}
.contact span{display:flex;align-items:center;gap:6px}
.contact .bullet{width:15px;height:15px;border-radius:50%;background:#fff;border:2px solid var(--gold);display:flex;align-items:center;justify-content:center}
.contact .bullet svg{width:8px;height:8px;fill:var(--heading)}
.stamp-box{position:absolute;left:631px;top:29px;width:125px;height:111px;border:1px solid #8c8c8c;background:#fff}
.address-line{position:absolute;left:539px;width:222px;height:1px;background:#9a9a9a}
.back-copy{position:absolute;left:46px;top:266px;font-size:13.5px;line-height:20px;color:var(--body);white-space:nowrap}
.tagline{position:absolute;left:47px;top:432px;font-weight:700;font-size:19.6px;color:#1a4aa0;white-space:nowrap}
</style>
</head>
<body>
<svg width="0" height="0" style="position:absolute" aria-hidden="true">
  <symbol id="tick" viewBox="0 0 24 24"><circle cx="11" cy="13" r="9" fill="none" stroke="#e3a93a" stroke-width="2"/><path d="M6.5 12.5l4 4L22 3" fill="none" stroke="#e3a93a" stroke-width="2.4" stroke-linecap="round" stroke-linejoin="round"/></symbol>
  <symbol id="i-home" viewBox="0 0 24 24"><path d="M12 3L2 12h3v9h5v-6h4v6h5v-9h3z"/></symbol>
  <symbol id="i-calc" viewBox="0 0 24 24"><path d="M6 2h12a2 2 0 0 1 2 2v16a2 2 0 0 1-2 2H6a2 2 0 0 1-2-2V4a2 2 0 0 1 2-2zm1 3v4h10V5zm0 7v2h2v-2zm4 0v2h2v-2zm4 0v2h2v-2zm-8 4v2h2v-2zm4 0v2h2v-2zm4 0v2h2v-2z"/></symbol>
  <symbol id="i-tag" viewBox="0 0 24 24"><path d="M3 3h9l9 9-9 9-9-9zm4 2.5a1.5 1.5 0 1 0 0 3 1.5 1.5 0 0 0 0-3z"/></symbol>
  <symbol id="i-grid" viewBox="0 0 24 24"><path d="M3 4h18v16H3zm2 2v3h4V6zm6 0v3h2V6zm4 0v3h4V6zM5 11v3h4v-3zm6 0v3h2v-3zm4 0v3h4v-3zM5 16v2h4v-2zm6 0v2h2v-2zm4 0v2h4v-2z"/></symbol>
  <symbol id="i-wallet" viewBox="0 0 24 24"><path d="M3 6a2 2 0 0 1 2-2h13v3H5v1h16v12H5a2 2 0 0 1-2-2zm13 8a1.5 1.5 0 1 0 3 0 1.5 1.5 0 0 0-3 0z"/></symbol>
  <symbol id="i-pen" viewBox="0 0 24 24"><path d="M3 17.3V21h3.7L18 9.7 14.3 6zM20.7 7a1 1 0 0 0 0-1.4l-2.3-2.3a1 1 0 0 0-1.4 0L15.2 5 19 8.8z"/></symbol>
  <symbol id="i-dollar" viewBox="0 0 24 24"><path d="M13 2v2.1c2.2.4 3.7 1.8 3.9 3.9h-2.4c-.2-1.2-1.2-1.9-2.5-1.9-1.5 0-2.5.7-2.5 1.800 1 .8 1.5 3 2 2.8.7 4.6 1.7 4.6 4.1 0 2-1.6 3.5-4.1 3.9V22h-2v-2.1c-2.5-.4-4.2-1.9-4.3-4.2h2.4c.2 1.3 1.3 2.2 3 2.2 1.6 0 2.7-.8 2.7-1.9 0-1.1-.9-1.6-3.1-2.1-2.6-.6-4.4-1.6-4.4-4 0-1.9 1.5-3.3 3.7-3.7V2z"/></symbol>
  <symbol id="i-phone" viewBox="0 0 24 24"><path d="M6.6 10.8a15.2 15.2 0 0 0 6.6 6.6l2.2-2.2a1 1 0 0 1 1-.25 11.4 11.4 0 0 0 3.6.57 1 1 0 0 1 1 1V20a1 1 0 0 1-1 1A17 17 0 0 1 3 4a1 1 0 0 1 1-1h3.5a1 1 0 0 1 1 1c0 1.250.2 2.45.57 3.57a1 1 0 0 1-.25 1z"/></symbol>
  <symbol id="i-globe" viewBox="0 0 24 24"><path d="M12 2a10 10 0 1 0 0 20 10 10 0 0 0 0-20zm-1 17.9A8 8 0 0 1 4.1 11H7c.1 3.3 1.5 6.4 4 8.9zM4.1 9A8 8 0 0 1 11 4.1C8.5 6.6 7.1 9.7 7 13zm8.9 10.9c2.5-2.5 3.9-5.6 4-8.9h2.9a8 8 0 0 1-6.9 8.9zM17 9c-.1-3.3-1.5-6.4-4-8.9A8 8 0 0 1 19.9 9z"/></symbol>
  <symbol id="i-mail" viewBox="0 0 24 24"><path d="M2 5h20v14H2zm2 2v.5l8 5 8-5V7z"/></symbol>
</svg>

<!-- FRONT -->
<section class="card card--front">
  <svg class="header-band" width="806" height="140" viewBox="0 0 806 140">
    <polygon points="0,0 511,0 422,138 0,138" fill="var(--navy)"/>
    <polygon points="511,0 541,0 453,138 423,138" fill="var(--gold)"/>
    <polygon points="546,0 558,0 469,138 457,138" fill="var(--sky)"/>
  </svg>
  <h1 class="headline" style="top:14px"><span class="gold">IS A PROPERTY LIEN</span><br>PUTTING YOUR HOME<br><span class="sky">AT RISK?</span></h1>
  <div class="brand"><span class="brand__dot"></span><span class="brand__name">Bluecove Lending Group, Inc.</span></div>

  <div class="photo photo--city" role="img" aria-label="Photo of a city waterfront skyline at sunset blending into a row of white townhouses"></div>

  <div class="front-icons">
    <div class="icon-item" style="left:47px;top:178px"><span class="ring"><svg width="17" height="17"><use href="#i-home"/></svg></span><span class="icon-label">HOA Liens</span></div>
    <div class="icon-item" style="left:160px;top:178px"><span class="ring"><svg width="15" height="15"><use href="#i-calc"/></svg></span><span class="icon-label">Tax Liens</span></div>
    <div class="icon-item" style="left:270px;top:178px"><span class="ring"><svg width="15" height="15"><use href="#i-tag"/></svg></span><span class="icon-label">Municipal<br>Charges</span></div>
    <div class="icon-item" style="left:383px;top:178px"><span class="ring"><svg width="15" height="15"><use href="#i-grid"/></svg></span><span class="icon-label">Other Property<br>Related Liens</span></div>
  </div>

  <div class="cream-band" style="top:212px;width:430px;height:53px;background:linear-gradient(90deg,var(--cream) 75%,rgba(251,236,198,0) 100%)"></div>
  <p class="lead-serif" style="top:219px">You may have options to resolve outstanding<br>liens and protect your home.</p>

  <h2 class="subhead" style="top:273px">A Refinance or Home Equity Line of Credit<br>(HELOC) may help you:</h2>
  <ul class="checklist" style="top:320px">
    <li><svg><use href="#tick"/></svg>Pay off qualifying liens</li>
    <li><svg><use href="#tick"/></svg>Consolidate debt into one manageable payment</li>
    <li><svg><use href="#tick"/></svg>Access your home's equity</li>
    <li><svg><use href="#tick"/></svg>Improve your financial flexibility</li>
    <li><svg><use href="#tick"/></svg>Avoid additional penalties, fees, or collection actions</li>
  </ul>
  <p class="closing" style="top:431px">Don't wait until the situation<br>becomes more difficult.</p>

  <div class="footer-bar">
    <svg width="806" height="43" viewBox="0 0 806 43" class="abs" style="left:0;top:0">
      <defs>
        <linearGradient id="goldFront" x1="0" y1="0" x2="0" y2="1"><stop offset="0" stop-color="var(--gold-light)"/><stop offset="1" stop-color="var(--gold-deep)"/></linearGradient>
        <linearGradient id="navyFront" x1="0" y1="0" x2="1" y2="0"><stop offset="0" stop-color="var(--navy-2)"/><stop offset="1" stop-color="var(--navy)"/></linearGradient>
      </defs>
      <rect width="806" height="43" fill="url(#navyFront)"/>
      <polygon points="0,0 405,0 355,43 0,43" fill="url(#goldFront)"/>
    </svg>
    <p class="footer-cta" style="font-size:15px">Call today for a confidential review of your options.</p>
    <div class="contact">
      <span><i class="bullet"><svg><use href="#i-phone"/></svg></i>(800) 641-2907 x 42</span>
      <span><i class="bullet"><svg><use href="#i-globe"/></svg></i>www.bluecovelending.com</span>
      <span>NMLS #738150</span>
    </div>
  </div>
</section>

<!-- BACK -->
<section class="card card--back">
  <svg class="header-band" width="806" height="102" viewBox="0 0 806 102">
    <polygon points="0,0 572,0 508,100 0,100" fill="var(--navy)"/>
    <polygon points="572,0 591,0 528,100 510,100" fill="var(--gold)"/>
    <polygon points="594,0 602,0 539,100 531,100" fill="var(--sky)"/>
  </svg>
  <h1 class="headline" style="top:14px;font-size:31.5px;line-height:39px"><span class="gold">YOUR HOME EQUITY COULD</span><br>BE THE SOLUTION</h1>

  <div class="stamp-box"></div>
  <div class="address-line" style="top:166px"></div>
  <div class="address-line" style="top:196px"></div>
  <div class="address-line" style="top:226px"></div>

  <div class="photo photo--advisor" role="img" aria-label="Photo of the loan officer seated in a dark suit and hat in front of a grey city skyline"></div>

  <h2 class="subhead" style="top:115px">If you have received notices regarding:</h2>
  <ul class="checklist" style="top:144px">
    <li><svg><use href="#tick"/></svg>Delinquent Property Taxes</li>
    <li><svg><use href="#tick"/></svg>HOA or Condo Association Assessments</li>
    <li><svg><use href="#tick"/></svg>Municipal Utility Liens</li>
    <li><svg><use href="#tick"/></svg>Special Assessments</li>
    <li><svg><use href="#tick"/></svg>Other Property-Related Obligations</li>
  </ul>

  <svg class="cream-band" style="top:259px" width="462" height="47" viewBox="0 0 462 47">
    <polygon points="0,0 460,0 420,46 0,46" fill="var(--cream)"/>
  </svg>
  <p class="back-copy">You may qualify for financing options designed to help<br>satisfy those obligations and bring your property current.</p>

  <h2 class="subhead" style="top:319px;font-size:15.9px">Our experienced mortgage professionals can review<br>your situation and discuss available programs, including:</h2>

  <div class="back-icons">
    <div class="icon-item" style="left:46px;top:395px"><span class="ring"><svg width="14" height="14"><use href="#i-wallet"/></svg></span><span class="icon-label">Cash-Out<br>Refinancing</span></div>
    <div class="icon-item" style="left:154px;top:395px"><span class="ring"><svg width="15" height="15"><use href="#i-home"/></svg></span><span class="icon-label">Home Equity<br>Lines of Credit<br>(HELOCs)</span></div>
    <div class="icon-item" style="left:273px;top:395px"><span class="ring"><svg width="14" height="14"><use href="#i-pen"/></svg></span><span class="icon-label">Home<br>Equity Loans</span></div>
    <div class="icon-item" style="left:390px;top:395px"><span class="ring"><svg width="15" height="15"><use href="#i-dollar"/></svg></span><span class="icon-label">Debt Consolidation<br>Solutions</span></div>
  </div>

  <p class="tagline">Free Consultation • No Obligation</p>

  <div class="footer-bar">
    <svg width="806" height="43" viewBox="0 0 806 43" class="abs" style="left:0;top:0">
      <defs>
        <linearGradient id="goldBack" x1="0" y1="0" x2="0" y2="1"><stop offset="0" stop-color="var(--gold-light)"/><stop offset="1" stop-color="var(--gold-deep)"/></linearGradient>
        <linearGradient id="navyBack" x1="0" y1="0" x2="1" y2="0"><stop offset="0" stop-color="var(--navy-2)"/><stop offset="1" stop-color="var(--navy)"/></linearGradient>
      </defs>
      <rect width="806" height="43" fill="url(#navyBack)"/>
      <polygon points="0,0 362,0 312,43 0,43" fill="url(#goldBack)"/>
    </svg>
    <p class="footer-cta" style="font-size:18px">Contact Marcus Whitfield today at</p>
    <div class="contact" style="gap:12px;font-size:10.5px;right:14px">
      <span><i class="bullet"><svg><use href="#i-phone"/></svg></i>(800) 641-2907 x 42</span>
      <span><i class="bullet"><svg><use href="#i-mail"/></svg></i>mwhitfield@bluecovelending.com</span>
      <span>(NMLS #84617)</span>
    </div>
  </div>
</section>
</body>
</html>
```